A5 & A3 Size flyer for OPEN NIGHT - Adult Education

We need a A5 & A3 formatted flyer for our upcoming OPEN NIGHT on Thursday, 17th November 2016 at our Blackburn campus. A3 for poster to display and A5 for flyers.

We are one of Victoria's leading private Reconised Training Organisations based in Melbourne, Victoria, Australia who specialise in the training of nationally recognised training courses in Pathology, Individual Support (Ageing, Home & Community, Disability), Allied Health Assistance, Health Services Assistance, Disability & Ageing Support.

The purpose of our open night is to gain prospective students for 2017 courses and the soul purpose of this flyer is to promote via emails, postal mail and hard copy drop offs to prospective clients, employers and our partnered networks for exposure.

The final design should reflect the colour scheme & style we have used in the attached already promoted designs. Should include our logo, address, event details, website and social media buttons (Facebook, Instagram, Youtube, Twitter, Pinterest & LinkedIn) Should be in line with our overall branding, as per our website www.brimcoveacademy.edu.au and ensure it is bold and engaging for promotional purposes.

Please also see our event listing for which ahs further information you may be able to use: https://bcaopenevening16.ticketnook.com.au

If you ahve any questions please send through a message!

Target Market(s)

Prospective students, employer organisations workforce

Industry/Entity Type

Adult

Colors
f37122
f78f20
ffc214
ffffff

Requirements
Must have
• See project description

```html
<!DOCTYPE html>
<html lang="en">
<head>
<meta charset="utf-8">
<title>Brimcove Academy – Open Night</title>
<link rel="stylesheet" href="https://fonts.googleapis.com/css2?family=Barlow+Condensed:ital,wght@1,900&family=Open+Sans:ital,wdth,wght@0,75..100,300..800;1,75..100,300..800&display=swap">
<style>
  :root {
    --orange: #f37122;
    --orange-light: #f78f20;
    --gold: #ffc214;
    --white: #ffffff;
    --ink: #4a4a4a;
    --dark: #1e1a18;
  }
  html, body { margin: 0; padding: 0; overflow: hidden; }
  body { background: #e8e8e8; }
  .flyer {
    position: relative; width: 849px; height: 1200px; overflow: hidden;
    background: var(--white); font-family: "Open Sans", sans-serif; font-stretch: 87.5%;
    color: var(--white);
  }
  .hero-photo {
    position: absolute; left: 0; top: 0; width: 849px; height: 930px;
    background: radial-gradient(ellipse at 70% 35%, #6d6a66 0%, #3c3632 40%, var(--dark) 80%);
  }
  .abs { position: absolute; margin: 0; white-space: nowrap; }
  .hl { right: 483px; text-align: right; line-height: 1; font-weight: 600; }
  .hl b { color: var(--orange-light); font-weight: 700; }
  .hl-1 { top: 52px; font-size: 37px; }
  .hl-2 { top: 86px; font-size: 27px; }
  .hl-2 b, .hl-3 b { font-size: 42px; }
  .hl-3 { top: 124px; font-size: 27px; }
  .hl-4 { top: 162px; font-size: 25px; }
  .event-title { top: 192px; font-family: "Barlow Condensed", sans-serif; font-style: italic; font-weight: 900; font-size: 60px; }
  .host { top: 262px; font-size: 31px; font-weight: 700; }
  .address { top: 293px; font-size: 15px; font-weight: 400; color: var(--orange-light); }
  .date { top: 312px; font-size: 50px; font-weight: 700; }
  .time { top: 362px; font-size: 32px; font-weight: 400; color: var(--gold); }
  .brand { left: 660px; top: 60px; width: 130px; text-align: center; }
  .brand-mark { width: 70px; height: 70px; border-radius: 50%; background: var(--orange); margin: 0 auto 16px; }
  .brand-name { font-size: 20px; font-weight: 600; color: var(--orange); line-height: 1.05; white-space: normal; }
  .brand-id { font-size: 6px; color: var(--orange); margin-top: 4px; }
  .intro { left: 72px; top: 530px; font-size: 19px; line-height: 1.12; }
  .cta { left: 72px; top: 582px; font-size: 30px; font-weight: 700; color: var(--orange-light); }
  .cta-sub { left: 72px; top: 618px; font-size: 19.5px; font-weight: 700; line-height: 1.05; }
  .para { left: 72px; font-size: 16px; line-height: 1.2; }
  .para.one { top: 679px; }
  .para.two { top: 736px; }
  .divider { left: 72px; top: 802px; width: 451px; height: 2px; background: var(--orange); }
  .courses { left: 70px; top: 828px; font-size: 21.5px; font-weight: 600; line-height: 1.16; }
  .courses span { margin-right: 12px; }
  .prize-band {
    left: 0; top: 920px; width: 849px; height: 80px; background: var(--orange-light);
    border-radius: 40px 0 40px 0;
  }
  .prize-text { left: 72px; top: 942px; font-size: 24px; font-weight: 700; text-shadow: 1px 2px 3px rgba(0,0,0,.35); }
  .prize-text b { font-size: 31px; }
  .tablet {
    left: 670px; top: 882px; width: 108px; height: 164px; border-radius: 8px;
    background: linear-gradient(160deg, #f2f2f2, #c9c9c9); box-shadow: 0 3px 8px rgba(0,0,0,.3);
  }
  .perks { left: 72px; top: 1012px; font-size: 12px; font-style: italic; font-weight: 700; color: var(--orange-light); line-height: 1.45; }
  .join { left: 72px; top: 1088px; font-size: 24px; color: var(--ink); }
  .book { left: 72px; top: 1112px; font-size: 38px; font-weight: 700; color: #5a5a5a; }
  .website { left: 520px; top: 1088px; width: 260px; text-align: right; font-size: 24px; font-weight: 600; color: var(--orange-light); }
  .social { left: 588px; top: 1120px; display: flex; gap: 3px; }
  .social span { width: 29px; height: 28px; display: block; }
</style>
</head>
<body>
<div class="flyer">
  <div class="hero-photo" role="img" aria-label="Photo of a group of adult students and staff seated in a circle in a bright classroom"></div>

  <p class="abs hl hl-1">ARE YOU LOOKING</p>
  <p class="abs hl hl-2">FOR A <b>REWARDING</b></p>
  <p class="abs hl hl-3"><b>CAREER IN</b> HEALTH</p>
  <p class="abs hl hl-4">&amp; COMMUNITY SERVICES?</p>
  <h1 class="abs hl event-title">OPEN NIGHT</h1>
  <p class="abs hl host">BRIMCOVE ACADEMY</p>
  <p class="abs hl address">LEVEL 2 41-45 STATION STREET, BLACKBURN</p>
  <p class="abs hl date">17 NOVEMBER</p>
  <p class="abs hl time">5:00 - 8:00PM</p>

  <div class="abs brand">
    <div class="brand-mark"></div>
    <div class="brand-name">brimcove academy</div>
    <div class="brand-id">TOID 40917</div>
  </div>

  <p class="abs intro">Are you looking for a career change? Not sure what to do once<br>high school has finished? Or simply wanting to UpSkill?</p>
  <h2 class="abs cta">COME ALONG AND JOIN US AT OUR OPEN NIGHT</h2>
  <p class="abs cta-sub">EXPLORE OUR CAMPUS, GET ALL YOUR QUESTIONS ANSWERED AND LEARN<br>WHAT CAREER AND COURSE OPTIONS ARE AVAILABLE TO YOU IN 2017.</p>
  <p class="abs para one">No matter what you are doing at the moment, the opportunity to complete a training program<br>and improve your career or even change it is completely is within your reach.</p>
  <p class="abs para two">We offer support and assistance through every stage of the training to ensure that you are able<br>to complete the course with confidence.</p>
  <div class="abs divider"></div>
  <p class="abs courses">
    <span>• PATHOLOGY</span><span>• AGED CARE</span><span>• DISABILITY</span><br>
    <span>• ALLIED HEALTH</span><span>• HEALTH SERVICES</span>
  </p>

  <div class="abs prize-band"></div>
  <p class="abs prize-text">Win yourself a <b>Lumo Tab Mini</b> &amp; more on the night!</p>
  <div class="abs tablet" role="img" aria-label="Photo of a small white tablet computer prize"></div>
  <p class="abs perks">• Lucky Door Prize Giveaways, Goodie Bags • Refreshments Provided • Tours of Campus &amp; Facilities<br>• Chat to Industry Experts &amp; Course Advisors • See a Live Tutorial Class in Action</p>

  <p class="abs join">Join us at our Open Night...</p>
  <p class="abs book">Book for free NOW!</p>
  <p class="abs website">brimcoveacademy.edu.au</p>
  <div class="abs social" aria-label="Social media links">
    <span style="background:#5a4a40"></span>
    <span style="background:#c8202f"></span>
    <span style="background:#3b5998"></span>
    <span style="background:#2aa3e0"></span>
    <span style="background:#0b77b5"></span>
    <span style="background:#d9242b"></span>
  </div>
</div>
</body>
</html>
```